New Digital Marketing Company Needs Web Design

Introduction

Pixelbrook gives advice to small businesses about their websites and digital marketing strategies and builds working relationships with clients to understand their business and maximise its online presence.

Pixelbrook offers services to support its clients needs such as: website auditing & search engine optimisation (SEO), Zorvani Promoline, Chatterloop advertising, newsletter development & management, online performance reporting, email setup & management, website hosting, maintenance & backup, web development, web updates & web design.

Design Specification

The site should have a clean & professional look and use the colour scheme from the logo (attached below).

The design should consist of 2 templates; The homepage & content page.

Homepage Design

The homepage should have a header with logo, contact number and email and menu. Followed underneath by a slider and then individual blocks for key services. Under the key services should be a testimonial block with 3 testimonials. Finally the footer with company details, menu links and location map.

Header Info:

Contact number: 01632 960418
Email: info@pixelbrook.co.uk

Menu: Home Services About Contact

Slider Design:

The slider should be full page and show an image with text.

Key Services:

The key services should have a relevant icon and brief description.

The key services are:

Digital Marketing

Website Hosting & Management

Website Health Check (SEO)

Website Updating & Development

Newsletter Management

Email Management

Note: Lorem Ipsum can be used for brief description...

Testimonials:

There should be 3 testimonials side by side and they should include a headshot image of the person giving the testimonial.

Note: Lorem Ipsum and sample images can be used for testimonials...

Footer:

The footer should have 3 sections:

Menu links:

Digital Marketing About
Zorvani Promoline Contact
Chatterloop Advertising Privacy Policy
Search Engine Optimisation (SEO) Terms & Conditions
Website Hosting FAQ
Newsletter Management

Company Information:

PixelBrook
14 Farrow Close
Bracknell
Berskhire
ZX47 3LT
Tel: 01632 960418

Chatterloop icon - Quillo icon - Guildnet icon

Location

Zorvani map

Footer Bottom:

Copyright message.

Content Design

The content design should have the common header and footer.

Each content page should have a banner for image with text description (page title).

The content page should have area for text description and area for a video display if available.

There should be a right column (possibly) for modules (latest blog, latest Chatterloop feeds, testimonial)
Updates

Reason: I have had to extend the deadline as could not review while on vacation and need to feedback to some designers for content page design. Many thanks for your understanding.

Target Market(s)

Industry/Entity Type

Digital

Number of Pages Required

2 page

Requirements
Must have
• The site should have a clean & professional look and use the colour scheme from the logo (attached below).
• The design should consist of 2 templates; The homepage & content page.

```html
<!DOCTYPE html>
<html lang="en">
<head>
<meta charset="utf-8">
<title>PixelBrook – About Our Company</title>
<link href="https://fonts.googleapis.com/css2?family=Open+Sans:ital,wght@0,400;0,600;0,700;1,400;1,600&family=Roboto+Condensed:wght@400;700&display=swap" rel="stylesheet">
<style>
:root{
  --plum:#6a1b4d;
  --plum-text:#7b2a5f;
  --ink:#333333;
  --body:#6b6b6b;
  --rule:#dedede;
  --panel:#f0f0f0;
  --blue:#2d5b9e;
  --social-blue:#3b55a8;
  --footer:#433a63;
  --footer-base:#2a2a2a;
  --white:#ffffff;
}
*{box-sizing:border-box;margin:0;padding:0}
html,body{width:677px;height:1200px;overflow:hidden;background:var(--white)}
body{position:relative;font-family:"Open Sans",Arial,sans-serif;color:var(--body)}
.abs{position:absolute}
.heading{font-family:"Roboto Condensed","Arial Narrow",sans-serif;font-weight:400;color:var(--ink)}

/* top bar */
.topbar{left:0;top:0;width:677px;height:18px}
.topbar-info{top:0;height:18px;font-size:7.5px;line-height:18px;color:#555;display:flex;gap:6px;align-items:center}

/* header */
.brand{left:56px;top:30px;display:flex;align-items:center;gap:5px}
.brand-dot{width:18px;height:18px;border-radius:50%;background:var(--plum)}
.brand-name{font-size:18px;font-weight:700;color:var(--plum);letter-spacing:-.2px}
.nav{top:18px;height:54px;left:0;width:677px}
.nav a{position:absolute;top:0;height:54px;line-height:56px;font-size:8px;color:#333;text-decoration:none;letter-spacing:.3px}
.nav a.active{color:var(--plum-text)}
.nav a.active::after{content:"";position:absolute;left:-1px;right:-1px;bottom:0;height:2px;background:var(--plum)}

/* hero */
.hero{left:0;top:72px;width:677px;height:214px;background:linear-gradient(90deg,#132433 0%,#1d3a4f 30%,#161b22 60%,#2a2c30 100%)}
.hero-title{left:56px;top:158px;font-family:"Roboto Condensed",sans-serif;font-weight:700;font-size:22px;line-height:23px;color:var(--white)}

/* main */
.h-welcome{left:56px;top:310px;font-size:17px}
.h-welcome span,.h-video{color:var(--plum-text)}
.copy{font-size:6.2px;line-height:11.6px;color:var(--body);width:372px}
.photo{background:linear-gradient(135deg,#b9c6cf,#e2e6ea 50%,#8e9aa6)}
.caption{font-size:8.5px;color:#333}
.h-video{left:56px;top:852px;font-size:17px}

/* sidebar */
.module-head{left:470px;width:152px;height:23px;background:var(--panel);border:1px solid var(--rule);display:flex;align-items:center;gap:5px;padding-left:7px}
.module-head .pin{width:10px;height:10px;border-radius:50%;border:2px solid var(--plum)}
.module-head .label{font-family:"Roboto Condensed",sans-serif;font-size:11.5px;color:#333}
.module-head .label b{font-weight:400;color:var(--blue)}
.blog-item{left:470px;width:152px;height:46px}
.blog-thumb{position:absolute;left:0;top:0;width:60px;height:46px;background:linear-gradient(135deg,#7f8b97,#c9d0d6 60%,#5e6873)}
.blog-title{position:absolute;left:68px;top:-1px;font-size:8px;color:#444}
.blog-time{position:absolute;left:68px;top:15px;font-size:5.5px;font-style:italic;font-weight:600;color:var(--plum-text)}
.blog-text{position:absolute;left:68px;top:25px;font-size:5.6px;line-height:9px;color:#666}

.feed{left:470px;top:470px;width:152px;height:327px;background:var(--social-blue);padding:0 3px 3px}
.feed-head{height:27px;display:flex;align-items:center;justify-content:center;gap:5px;color:var(--white);font-weight:700;font-size:9.5px}
.feed-head i{width:7px;height:7px;background:var(--white)}
.feed-body{position:relative;background:var(--white);height:294px;overflow:hidden;padding:7px 10px 0 7px;font-size:5.8px;color:#777}
.feed-page{font-size:8px;color:var(--social-blue);font-weight:600;margin-bottom:8px}
.feed-meta{display:flex;gap:5px;margin:5px 0 6px}
.feed-meta .av{width:17px;height:17px;border:1px solid var(--rule);border-radius:2px;position:relative}
.feed-meta .av::after{content:"";position:absolute;left:4px;top:4px;width:7px;height:7px;border-radius:50%;background:var(--plum)}
.feed-meta b{display:block;font-weight:600;color:#333;font-size:5.8px}
.feed-meta small{color:var(--social-blue);font-size:4.8px}
.feed-img{height:84px;background:linear-gradient(135deg,#4fa8a0,#e9b44a 55%,#d5574e)}
.feed-note{border:1px solid var(--rule);border-top:0;padding:5px 6px;line-height:9.6px;margin-bottom:12px}
.feed-note.boxed{border-top:1px solid var(--rule);padding:6px}
.scroll{position:absolute;right:2px;top:30px;width:5px;height:255px;background:#f3f3f3}
.scroll i{position:absolute;left:0;top:30px;width:5px;height:60px;background:#c8c8c8}

.quote{left:470px;top:840px;width:152px;height:85px;background:var(--panel);border:1px solid var(--rule);padding:11px 8px 0 10px;font-size:5.9px;line-height:11.4px;color:#777}
.quote::after{content:"";position:absolute;left:80px;bottom:-7px;border:7px solid transparent;border-bottom:0;border-top-color:var(--panel)}
.avatar{left:482px;top:937px;width:42px;height:42px;border-radius:50%;background:linear-gradient(160deg,#d8c9bd,#8b7a6c);border:2px solid #eee}
.person{left:537px;top:947px;font-size:8px;font-style:italic;color:#555}
.person small{display:block;font-size:6.5px;font-weight:600;color:#555}

/* footer */
.footer{left:0;top:1014px;width:677px;height:153px;background:var(--footer);color:var(--white)}
.footer-brand{left:56px;top:1036px;display:flex;align-items:center;gap:5px}
.footer-brand .brand-dot{background:var(--white)}
.footer-brand .brand-name{color:var(--white)}
.footer-line{left:56px;font-size:7px;line-height:11px;color:var(--white);display:flex;gap:10px}
.footer-line svg{flex:none;margin-top:1px}
.footer-head{font-family:"Roboto Condensed",sans-serif;font-size:10.5px;color:var(--white)}
.map{left:225px;top:1058px;width:196px;height:90px;background:linear-gradient(135deg,#cfd8c4,#e6e4dd 45%,#b8cbe0);border:2px solid #ddd}
.links{left:451px;top:1058px;list-style:none;font-size:6.9px;line-height:13.6px}
.base{left:0;top:1167px;width:677px;height:33px;background:var(--footer-base)}
.copyright{left:56px;top:1178px;font-size:6.9px;color:var(--white)}
.social{top:1176px;width:15px;height:15px;border-radius:50%;border:1px solid #bbb}
</style>
</head>
<body>

<!-- top bar -->
<svg class="abs topbar" width="677" height="18" viewBox="0 0 677 18" aria-hidden="true">
  <rect width="677" height="18" fill="#efefef"/>
  <polygon points="0,0 366,0 358,18 0,18" fill="#6a1b4d"/>
</svg>
<div class="abs topbar-info" style="left:410px">
  <svg width="7" height="7" viewBox="0 0 10 10"><path d="M2 1l2 2-1 1.5c.6 1.2 1.4 2 2.5 2.5L7 6l2 2-1.5 1.5C4.5 9 1 5.5.5 2.5z" fill="#555"/></svg>
  <span>+01632 960418</span>
</div>
<div class="abs topbar-info" style="left:505px">
  <svg width="8" height="6" viewBox="0 0 10 7"><rect x=".5" y=".5" width="9" height="6" fill="none" stroke="#555"/><path d="M.5.5l4.5 3.5L9.5.5" fill="none" stroke="#555"/></svg>
  <span>Email: info@pixelbrook.co.uk</span>
</div>

<!-- header -->
<div class="abs brand"><span class="brand-dot"></span><span class="brand-name">PixelBrook</span></div>
<nav class="abs nav">
  <a href="#" style="left:409px">HOME</a>
  <a href="#" class="active" style="left:455px">ABOUT US</a>
  <a href="#" style="left:518px">SERVICES</a>
  <a href="#" style="left:573px">CONTACT US</a>
</nav>

<!-- banner -->
<div class="abs hero" role="img" aria-label="Banner photo: hands holding a tablet with a cloud of floating devices above it"></div>
<h1 class="abs hero-title">ABOUT OUR<br>COMPANY</h1>

<!-- main column -->
<h2 class="abs heading h-welcome">WELCOME TO <span>PIXELBROOK</span></h2>
<p class="abs copy" style="left:56px;top:335px">Sed ut perspiciatis unde omnis iste natus error sit voluptatem accusantium doloremque laudantium, totam rem aperiam, eaque ipsa quae ab illo inventore veritatis et quasi architecto beatae vitae dicta sunt explicabo. Nemo enim ipsam voluptatem quia voluptas sit aspernatur aut odit aut fugit, sed quia consequuntur magni dolores eos qui ratione voluptatem sequi nesciunt. Neque porro quisquam est, qui dolorem ipsum quia dolor sit amet, consectetur</p>
<p class="abs copy" style="left:56px;top:387px">Sed ut perspiciatis unde omnis iste natus error sit voluptatem accusantium doloremque laudantium, totam rem aperiam, eaque ipsa quae ab illo inventore veritatis et quasi architecto beatae vitae dicta sunt explicabo. Nemo enim ipsam voluptatem quia voluptas sit aspernatur aut odit aut fugit, sed quia consequuntur magni dolores eos qui ratione voluptatem sequi nesciunt. Neque porro quisquam est, qui dolorem ipsum quia dolor sit amet, consectetur</p>

<div class="abs photo" style="left:56px;top:456px;width:184px;height:106px" role="img" aria-label="Photo: presenter at a whiteboard chart in a meeting room"></div>
<div class="abs photo" style="left:262px;top:456px;width:184px;height:106px" role="img" aria-label="Photo: smiling colleagues talking at a meeting table"></div>
<h3 class="abs heading caption" style="left:56px;top:572px">DIGITAL MARKETING ABOUT</h3>
<h3 class="abs heading caption" style="left:262px;top:572px">ZORVANI PROMOLINE CONTACT</h3>
<p class="abs copy" style="left:56px;top:588px;width:184px">Sed ut perspiciatis unde omnis iste natus error sit luptatem accusantium doloremque laudantium, totam rem aperiam, eaque ipsa quae ab illo inventore veritatis</p>
<p class="abs copy" style="left:262px;top:588px;width:184px">Sed ut perspiciatis unde omnis iste natus error sit luptatem accusantium doloremque laudantium, totam rem aperiam, eaque ipsa quae ab illo inventore veritatis</p>

<div class="abs photo" style="left:56px;top:641px;width:390px;height:198px;background:linear-gradient(135deg,#8a6a4c,#d9cfc4 45%,#7c8793)" role="img" aria-label="Video still: people at a wooden desk with a laptop and a tablet showing a bar chart"></div>
<svg class="abs" style="left:238px;top:731px" width="26" height="26" viewBox="0 0 26 26" aria-label="Play video">
  <circle cx="13" cy="13" r="11.5" fill="rgba(255,255,255,.55)" stroke="#444" stroke-width="1.5"/>
  <path d="M10 8l8 5-8 5z" fill="#444"/>
</svg>

<h2 class="abs heading h-video">PIXELBROOK VIDEO</h2>
<p class="abs copy" style="left:56px;top:876px">Sed ut perspiciatis unde omnis iste natus error sit voluptatem accusantium doloremque laudantium, totam rem aperiam, eaque ipsa quae ab illo inventore veritatis et quasi architecto beatae vitae dicta sunt explicabo. Nemo enim ipsam voluptatem quia voluptas sit aspernatur aut odit aut fugit, sed quia consequuntur magni dolores eos qui ratione voluptatem sequi nesciunt. Neque porro quisquam est, qui dolorem ipsum quia dolor sit amet, consectetur</p>
<p class="abs copy" style="left:56px;top:928px">Sed ut perspiciatis unde omnis iste natus error sit voluptatem accusantium doloremque laudantium, totam rem aperiam, eaque ipsa quae ab illo inventore veritatis et quasi architecto beatae vitae dicta sunt explicabo. Nemo enim ipsam voluptatem quia voluptas sit aspernatur aut odit aut fugit, sed quia consequuntur magni dolores eos qui ratione voluptatem sequi nesciunt. Neque porro quisquam est, qui dolorem ipsum quia dolor sit amet, consectetur</p>

<!-- sidebar -->
<div class="abs module-head" style="top:314px"><span class="pin"></span><span class="label">LATEST <b>BLOG</b></span></div>
<div class="abs blog-item" style="top:349px">
  <div class="blog-thumb" role="img" aria-label="Photo: two businessmen reviewing papers"></div>
  <div class="blog-title">Nemo Enim Ipsam</div>
  <div class="blog-time">3 MINUTES AGO</div>
  <div class="blog-text">Lorem ipsum dolor sit amet, consectetur adipiscing elit,</div>
</div>
<div class="abs blog-item" style="top:407px">
  <div class="blog-thumb" role="img" aria-label="Photo: two businessmen reviewing papers"></div>
  <div class="blog-title">Nemo Enim Ipsam</div>
  <div class="blog-time">3 MINUTES AGO</div>
  <div class="blog-text">Lorem ipsum dolor sit amet, consectetur adipiscing elit,</div>
</div>

<div class="abs feed">
  <div class="feed-head"><i></i>Chatterloop</div>
  <div class="feed-body">
    <div class="feed-page">Pixelbrook</div>
    <div>Pixelbrook Sed ut perspiciatis</div>
    <div class="feed-meta"><span class="av"></span><div><b>Pixelbrook</b><small>Like · Reply · 1 · 10 Oct at 22:18</small></div></div>
    <div class="feed-img" role="img" aria-label="Post photo: hands on a table with colourful social media stickers"></div>
    <div class="feed-note">Sed ut perspiciatis unde omnis iste natus error sit voluptatem</div>
    <div>Pixelbrook Sed ut perspiciatis</div>
    <div class="feed-meta"><span class="av"></span><div><b>Pixelbrook</b><small>Like · Reply · 1 · 10 Oct at 22:18</small></div></div>
    <div class="feed-note boxed">Sed ut perspiciatis unde omnis iste natus error sit voluptatem accusantium doloremque laudantium, totam rem aperiam, eaque ipsa</div>
    <div class="scroll"><i></i></div>
  </div>
</div>

<div class="abs module-head" style="top:812px"><span class="pin"></span><span class="label">TESTIMONIAL</span></div>
<div class="abs quote">
  <span style="font-size:11px;color:#bbb;font-family:Georgia,serif">&ldquo;</span> Sed ut perspiciatis unde omnis iste natus error sit voluptatem accusantium doloremque laudantium, totam rem aperiam, eaque ipsa quae ab illo inventore veritatis et quasi architecto beatae vitae
</div>
<div class="abs avatar" role="img" aria-label="Headshot of the client giving the testimonial"></div>
<div class="abs person">Mara Quilby<small>Pixelbrook</small></div>

<!-- footer -->
<footer>
  <div class="abs footer"></div>
  <div class="abs footer-brand"><span class="brand-dot"></span><span class="brand-name">PixelBrook</span></div>
  <div class="abs footer-line" style="top:1075px">
    <svg width="9" height="12" viewBox="0 0 9 12"><path d="M4.5 11.5S1 7 1 4.5a3.5 3.5 0 017 0C8 7 4.5 11.5 4.5 11.5z" fill="none" stroke="#fff"/><circle cx="4.5" cy="4.5" r="1.3" fill="#fff"/></svg>
    <span>Pixelbrook 14 Farrow Close<br>Bracknell Berskhire ZX47 3LT</span>
  </div>
  <div class="abs footer-line" style="top:1103px">
    <svg width="10" height="10" viewBox="0 0 10 10"><path d="M2 1l2 2-1 1.5c.6 1.2 1.4 2 2.5 2.5L7 6l2 2-1.5 1.5C4.5 9 1 5.5.5 2.5z" fill="none" stroke="#fff" stroke-width=".8"/></svg>
    <span>Phone : 01632 960418</span>
  </div>
  <div class="abs footer-line" style="top:1122px">
    <svg width="10" height="8" viewBox="0 0 10 8"><rect x=".5" y=".5" width="9" height="7" fill="none" stroke="#fff"/><path d="M.5.5l4.5 4 4.5-4" fill="none" stroke="#fff"/></svg>
    <span>Email: info@pixelbrook.co.uk</span>
  </div>

  <h4 class="abs footer-head" style="left:224px;top:1035px">OUR LOCATION</h4>
  <div class="abs map" role="img" aria-label="Zorvani street map of the office location in Bracknell"></div>

  <h4 class="abs footer-head" style="left:451px;top:1035px">QUICK LINKS</h4>
  <ul class="abs links">
    <li>Digital Marketing About</li>
    <li>Zorvani Promoline Contact</li>
    <li>Chatterloop Advertising Privacy Policy</li>
    <li>Search Engine Optimisation (SEO) Terms &amp; Conditions</li>
    <li>Website Hosting FAQ</li>
    <li>Newsletter Management</li>
  </ul>

  <div class="abs base"></div>
  <p class="abs copyright">Copyright © Pixelbrook 2016. All rights reserved.</p>
  <a class="abs social" href="#" style="left:588px" aria-label="Guildnet"></a>
  <a class="abs social" href="#" style="left:606px" aria-label="Quillo"></a>
</footer>

</body>
</html>
```